DL Card Flyer

Goal: Professional, clean, sharp and trendy.
Business: For a real estate Agent.
Agency: HOVEL (can get logo online)
Measurements: 20cm x 9cm

Please use the attachments as a guide as to what I would like the flyer to look like. It will be 2 sided. The first side will be with the girl and the second will be information about myself and how to contact me.

Target Market(s)

Target market: To have prestige property owners (particularly houses on the water) to sell their house (whether it be immediate or in the near future).

Industry/Entity Type

Real Estate

Requirements
Must have
• -Character, class and sophistication, with a bit of fun.
-Doesn't need to look like another property brochure-needs to be original.
-Must have the HOVEL logo.
-Needs to stand out from other brochures!
-Double sided (with a space for my photo on the back with my BIO)
-Very similar to the flyer attachments
-Doesn't need to feature a house!
-MUST HAVE ATTACHED HEADSHOT PHOTOGRAPH

Copy:
Missing opportunities in today’s property market is not an option. There are many unique and diverse opportunities available to you, but without all the relevant information, you could be missing out.

I’m thrilled to report that currently, the real estate market has a positive outlook. During the past 6 months, the market has rebounded wonderfully, and numerous homeowners who are waiting it out are realizing now is the time to take action.

Having worked and studied in both Europe and Asia, I have learned that communication, commitment and understanding the individual needs of each client are the keys to mutual success.

I understand the importance of careful consideration and diversification and staying ahead in the property industry and I’m happy to work with you to combine these components into an advantageous real estate transaction.
Nice to have
• -Second side needs to have information about myself.
-Name, Mobile, Email, Fax, Address (and Po Box)
-I like the fonts Lato, Aleo, Hagin, Franchise, Rex etc.

I have attached a example of the brochure that I wouldn't mind if it was replicated.

```html
<!DOCTYPE html>
<html lang="en">
<head>
<meta charset="utf-8">
<title>DL Card Flyer – Hovel</title>
<link rel="stylesheet" href="https://fonts.googleapis.com/css2?family=Lato:ital,wght@0,300;0,400;0,700;0,900;1,700&family=Kaushan+Script&family=Montserrat:wght@700&display=swap">
<style>
  :root {
    --page: #ffffff;
    --teal: #1591a8;
    --teal-deep: #0b7d93;
    --teal-ink: #146a7c;
    --ink: #111111;
    --white: #ffffff;
    --slate: #2f3335;
    --slate-dark: #222527;
    --blue: #2474bd;
    --sea: #1b5f6b;
    --grey-disc: #3b4246;
    --rule: #2b2b2b;
  }
  * { box-sizing: border-box; margin: 0; padding: 0; }
  html, body { width: 1200px; height: 1000px; overflow: hidden; background: var(--page); }
  body { position: relative; font-family: "Lato", sans-serif; }

  .card { position: absolute; overflow: hidden; box-shadow: 0 1px 4px rgba(0,0,0,.18); }

  /* ---------- front side ---------- */
  .card--front { left: 128px; top: 59px; width: 405px; height: 899px; background: var(--white); }
  .front-hero {
    position: absolute; left: 0; top: 0; width: 405px; height: 606px;
    background: linear-gradient(180deg, var(--teal) 0%, var(--teal-deep) 100%);
  }
  .hero-photo {
    position: absolute; left: 30px; top: 290px; width: 375px; height: 316px;
    background: radial-gradient(ellipse at 50% 45%, #d9b9a4 0%, #4fb1c0 45%, rgba(21,145,168,0) 75%);
  }
  .front-headline {
    position: absolute; left: 0; top: 24px; width: 405px;
    color: var(--white); font-weight: 300; font-size: 34px; line-height: 44px; text-align: center;
  }
  .front-tagline {
    position: absolute; left: 26px; top: 262px;
    font-family: "Kaushan Script", cursive; color: var(--white); font-size: 23px;
    transform: rotate(-6deg); transform-origin: left center; white-space: nowrap;
  }
  .seal { position: absolute; left: 302px; top: 584px; width: 90px; height: 90px; }
  .offer-lead {
    position: absolute; left: 0; top: 642px; width: 405px; text-align: center;
    font-family: "Kaushan Script", cursive; color: var(--teal-ink); font-size: 30px; line-height: 36px;
  }
  .offer-title {
    position: absolute; left: 0; top: 680px; width: 405px; text-align: center;
    font-family: "Montserrat", sans-serif; font-weight: 700; font-size: 23px; color: var(--ink); letter-spacing: -.2px;
  }
  .offer-title em { font-style: normal; color: var(--teal-ink); }
  .offer-rule { position: absolute; left: 97px; top: 713px; width: 218px; height: 4px; background: var(--rule); }
  .offer-body {
    position: absolute; left: 45px; top: 732px; width: 315px; text-align: center;
    font-size: 12.5px; line-height: 16px; color: var(--ink);
  }
  .offer-body p { margin-bottom: 6px; }

  /* ---------- back side ---------- */
  .card--back { left: 579px; top: 57px; width: 406px; height: 901px; background: var(--slate); }
  .back-shapes { position: absolute; left: 0; top: 0; width: 406px; height: 781px; }
  .agent-photo {
    position: absolute; left: 6px; top: 283px; width: 268px; height: 498px;
    background: linear-gradient(180deg, #6b4a38 0%, #c79a80 30%, #3a2a24 60%, #161616 100%);
    border-radius: 40% 40% 0 0 / 22% 22% 0 0;
  }
  .back-intro {
    position: absolute; left: 20px; top: 47px; width: 350px;
    color: var(--white); font-weight: 700; font-size: 12.6px; line-height: 17px;
  }
  .back-bio {
    position: absolute; left: 20px; top: 131px; width: 340px;
    color: var(--white); font-weight: 300; font-size: 13px; line-height: 17.2px;
  }
  .back-bio .end { display: block; text-align: right; padding-right: 2px; }
  .back-quote {
    position: absolute; right: 37px; top: 307px; width: 150px; text-align: right;
    color: var(--white); font-weight: 700; font-style: italic; font-size: 14.5px; line-height: 19px;
  }
  .agent-name {
    position: absolute; right: 38px; top: 686px; color: var(--white); font-size: 17px; font-weight: 300;
  }
  .agent-name b { font-weight: 700; }
  .contact-list {
    position: absolute; right: 38px; top: 711px; width: 320px; color: var(--white); font-size: 13.5px; line-height: 21px;
  }
  .contact-row { display: flex; justify-content: flex-end; gap: 20px; }
  .contact-item { display: inline-flex; align-items: center; gap: 4px; }
  .contact-item svg { width: 15px; height: 15px; fill: var(--white); }
  .back-footer { position: absolute; left: 0; top: 781px; width: 406px; height: 120px; background: var(--slate-dark); }
  .brand { position: absolute; left: 0; top: 40px; width: 406px; display: flex; justify-content: center; align-items: center; gap: 14px; }
  .brand-dot { width: 36px; height: 36px; border-radius: 50%; background: #d8d8d8; }
  .brand-name { color: var(--white); font-weight: 700; font-size: 28px; letter-spacing: 1px; }
</style>
</head>
<body>

<section class="card card--front" aria-label="Flyer front">
  <div class="front-hero" role="img" aria-label="Teal diamond-pattern background"></div>
  <div class="hero-photo" role="img" aria-label="Photograph of a cheering woman with glasses and a teal top, fists raised"></div>
  <h1 class="front-headline">We don’t focus on<br>selling as many<br>properties as we can,<br>we aim to sell for as<br>much as we can!</h1>
  <p class="front-tagline">- selling you your next dream</p>
  <svg class="seal" viewBox="0 0 90 90" aria-hidden="true">
    <circle cx="45" cy="45" r="43" fill="#e9e9e9" stroke="#bdbdbd" stroke-width="2"/>
    <circle cx="45" cy="45" r="35" fill="#ffffff" stroke="#2b79b8" stroke-width="4"/>
  </svg>
  <p class="offer-lead">Did you know we offer</p>
  <h2 class="offer-title">A <em>FREE</em> EQUITY CHECK SERVICE</h2>
  <div class="offer-rule"></div>
  <div class="offer-body">
    <p>This is the Studio's version of Lorem Ipsum. Proin gravida nibh vel velit auctor aliquet.</p>
    <p>Aenean sollicitudin, lorem quis bibendum auctor, nisi elit</p>
    <p>consequat ipsum, nec sagittis sem nibh id elit. Duis sed odio sit amet nibh vulputate cursus a sit amet mauris.</p>
    <p>Morbi accumsan ipsum velit. Nam nec tellus a</p>
  </div>
</section>

<section class="card card--back" aria-label="Flyer back">
  <svg class="back-shapes" viewBox="0 0 406 781" aria-hidden="true">
    <circle cx="380" cy="370" r="200" fill="var(--blue)"/>
    <circle cx="285" cy="560" r="85" fill="var(--sea)"/>
    <circle cx="370" cy="680" r="75" fill="var(--grey-disc)"/>
  </svg>
  <div class="agent-photo" role="img" aria-label="Headshot of the agent, a smiling woman with long dark hair in a black top"></div>
  <p class="back-intro">Missing opportunities in today’s property market is not an option. There are many unique and diverse opportunities available to you, but without all the relevant information, you could be missing out.</p>
  <p class="back-bio">I’m thrilled to report that currently, the real estate market has a positive outlook. During the past 6 months, the market has rebounded wonderfully, and numerous homeowners who are waiting it out are realizing now is the time to take action.<br>Having worked and studied in both Europe and Asia, I have learned that communication, commitment and understanding the individual needs of each client are <span class="end">the keys to mutual success.</span></p>
  <blockquote class="back-quote">“I understand the importance of careful consideration and diversification and staying ahead in the property industry and I’m happy to work with you to combine these components into an advantageous real estate transaction.”</blockquote>
  <p class="agent-name"><b>FirstName</b> LastName</p>
  <div class="contact-list">
    <div class="contact-row">
      <span class="contact-item"><svg viewBox="0 0 24 24"><path d="M6.6 10.8a15 15 0 0 0 6.6 6.6l2.2-2.2c.3-.3.7-.4 1-.2 1.1.4 2.3.6 3.6.6.6 0 1 .4 1 1V20c0 .6-.4 1-1 1A17 17 0 0 1 3 4c0-.6.4-1 1-1h3.5c.6 0 1 .4 1 1 0 1.3.2 2.5.6 3.6.1.3 0 .7-.2 1z"/></svg>+01 234-5678</span>
      <span class="contact-item"><svg viewBox="0 0 24 24"><path d="M3 5h18v14H3zM5 7v2h3V7zm5 0v2h3V7zm5 0v2h4V7zM5 11v2h3v-2zm5 0v2h3v-2zm5 0v2h4v-2zM5 15v2h3v-2zm5 0v2h3v-2zm5 0v2h4v-2z"/></svg>+01 910-2345</span>
    </div>
    <div class="contact-row">
      <span class="contact-item"><svg viewBox="0 0 24 24"><path d="M2 5h20v14H2zm2 2v.4l8 5 8-5V7zm0 2.8V17h16V9.8l-8 5z"/></svg>Me@Email.com</span>
      <span class="contact-item"><svg viewBox="0 0 24 24"><path d="M3 3h16v10H11v8H9v-8H3z"/></svg>P.O. BOX 1234567</span>
    </div>
  </div>
  <div class="back-footer">
    <div class="brand">
      <span class="brand-dot" aria-hidden="true"></span>
      <span class="brand-name">HOVEL</span>
    </div>
  </div>
</section>

</body>
</html>
```